Car wrap design for Boxwillow

We need a car wrap design for our Van (Korvana Stelt Hi roof Black color). We are freight expert sending international parcels from China to New Zealand. Consonlidating parcels and save money for customers. We would like to see designs that use the color match our logo and final design should communicate our service and tell customer we are expert,Specializing in International Freight Forwarding within China's Trade Line.

Our website: www.boxwillow.co.nz Our phone: 09 4815396, We specialized: Sea Parcels, Air Parcels, Loose Cargo
in China Trade line

Target Market(s)

New Zealand small business

Industry/Entity Type

International Freight Fowarding

• Please refer to brand guideline

Requirements
Must have
• logo, website, phone, what we do (Sea Parcels, Air Parcels, Loose Cargo)
Nice to have
• Beautiful Lines or Graphics

```html
<!DOCTYPE html>
<html lang="en">
<head>
<meta charset="utf-8">
<title>Boxwillow – Korvana Stelt Van Wrap</title>
<link rel="stylesheet" href="https://fonts.googleapis.com/css2?family=Anton&family=Poppins:wght@500;700&display=swap">
<style>
  :root {
    --wrap-red: #e3101b;
    --wrap-red-deep: #b80c14;
    --wrap-black: #121212;
    --wrap-white: #ffffff;
    --glass: #c8cdd1;
    --backdrop: #eeeeee;
    --ink-dark: #1b1b1b;
  }
  html, body {
    margin: 0;
    width: 1200px;
    height: 1200px;
    overflow: hidden;
    background: var(--backdrop);
  }
  .wrap-sheet { display: block; width: 1200px; height: 1200px; }
  .brand-name {
    font-family: "Anton", "Impact", sans-serif;
    font-size: 138px;
    letter-spacing: 1px;
  }
  .service-line {
    font-family: "Poppins", "Arial", sans-serif;
    font-weight: 700;
    font-size: 19px;
    fill: var(--wrap-white);
    letter-spacing: 0.5px;
  }
  .phone-number {
    font-family: "Poppins", "Arial", sans-serif;
    font-weight: 700;
    font-size: 27px;
    letter-spacing: 3px;
  }
  .web-address {
    font-family: "Poppins", "Arial", sans-serif;
    font-weight: 500;
    font-size: 16px;
  }
  .body-black { fill: var(--wrap-black); }
  .body-red { fill: var(--wrap-red); }
  .window-glass { fill: var(--glass); }
  .route-line { fill: none; stroke: var(--wrap-white); stroke-width: 1.6; stroke-dasharray: 4 4; opacity: 0.8; }
  .map-area { fill: url(#map-tone); }
  .pin-icon { fill: var(--wrap-white); }
  .outline { fill: none; stroke: #9a9a9a; stroke-width: 1.5; }

  .van-light .brand-name { fill: var(--wrap-red); }
  .van-light .phone-number { fill: var(--wrap-red); }
  .van-light .web-address { fill: var(--ink-dark); }
  .van-light .panel-base { fill: var(--wrap-white); }
  .van-light .trim-stripe { fill: var(--wrap-red); }

  .van-red .brand-name { fill: var(--wrap-black); }
  .van-red .phone-number { fill: var(--wrap-white); }
  .van-red .web-address { fill: var(--wrap-white); }
  .van-red .panel-base { fill: var(--wrap-red); }
  .van-red .trim-stripe { fill: var(--wrap-black); }
  .van-red .band-edge { fill: var(--wrap-black); }
</style>
</head>
<body>
<svg class="wrap-sheet" viewBox="0 0 1200 1200" xmlns="http://www.w3.org/2000/svg">
  <defs>
    <path id="van-shape" d="M10 30 Q12 8 40 6 L700 4 Q760 6 800 40 L930 150 Q1000 165 1030 215 L1060 260 L1068 330 L1064 392 L1000 392 A75 75 0 0 0 850 392 L310 392 A75 75 0 0 0 160 392 L10 392 Z"/>
    <clipPath id="van-clip"><use href="#van-shape"/></clipPath>
    <linearGradient id="map-tone" x1="0" y1="0" x2="1" y2="1">
      <stop offset="0" stop-color="#e3101b"/>
      <stop offset="1" stop-color="#b80c14"/>
    </linearGradient>
    <g id="pin">
      <path class="pin-icon" d="M0 -14 a7 7 0 0 1 7 7 c0 5 -7 12 -7 12 s-7 -7 -7 -12 a7 7 0 0 1 7 -7z M0 -10 a3 3 0 1 0 0.01 0z" fill-rule="evenodd"/>
    </g>
  </defs>

  <!-- Van one: white body panel -->
  <g class="van-panel van-light" transform="translate(65 70)">
    <g clip-path="url(#van-clip)">
      <rect class="panel-base" x="0" y="0" width="1080" height="400"/>
      <polygon class="body-black" points="0,-10 1080,-10 1080,193 0,24"/>
      <polygon class="trim-stripe" points="322,46 760,128 760,140 322,52"/>
      <polygon class="body-red" points="0,171 1080,403 1080,445 0,213"/>
      <polygon class="body-black" points="0,213 1080,445 1080,420 0,420"/>
      <rect class="body-black" x="1010" y="330" width="70" height="70"/>
      <rect class="map-area" role="img" aria-label="New Zealand map area" x="40" y="240" width="110" height="110" rx="26"/>
      <rect class="map-area" role="img" aria-label="China map area with stars" x="320" y="318" width="225" height="90" rx="30"/>
      <path class="route-line" d="M103 319 Q230 200 359 331"/>
      <use href="#pin" x="100" y="322"/>
      <use href="#pin" x="356" y="335"/>
    </g>
    <polygon class="window-glass" points="760,99 905,100 970,160 973,199 760,199"/>
    <text class="brand-name" x="54" y="167" textLength="680" lengthAdjust="spacingAndGlyphs" transform="rotate(10.4 54 167)">BOXWILLOW</text>
    <text class="service-line" x="50" y="209" textLength="630" lengthAdjust="spacingAndGlyphs" transform="rotate(12.1 50 209)">SEA PARCELS, AIR PARCELS, LOOSE CARGO IN CHINA TRADE LINE</text>
    <text class="phone-number" x="788" y="262" transform="rotate(8 788 262)">09 4815396</text>
    <text class="web-address" x="792" y="286" transform="rotate(8 792 286)">www.boxwillow.co.nz</text>
    <use class="outline" href="#van-shape"/>
  </g>

  <!-- Van two: red body panel -->
  <g class="van-panel van-red" transform="translate(65 665)">
    <g clip-path="url(#van-clip)">
      <rect class="panel-base" x="0" y="0" width="1080" height="400"/>
      <polygon class="body-black" points="0,-10 1080,-10 1080,193 0,24"/>
      <polygon class="trim-stripe" points="322,46 760,128 760,140 322,52"/>
      <polygon class="band-edge" points="0,164 1080,396 1080,403 0,171"/>
      <polygon class="body-red" points="0,171 1080,403 1080,445 0,213"/>
      <polygon class="band-edge" points="0,213 1080,445 1080,452 0,220"/>
      <polygon class="body-black" points="0,220 1080,452 1080,420 0,420"/>
      <rect class="body-black" x="1010" y="330" width="70" height="70"/>
      <rect class="map-area" role="img" aria-label="New Zealand map area" x="40" y="240" width="110" height="110" rx="26"/>
      <rect class="map-area" role="img" aria-label="China map area with stars" x="320" y="318" width="225" height="90" rx="30"/>
      <path class="route-line" d="M103 319 Q230 200 359 331"/>
      <use href="#pin" x="100" y="322"/>
      <use href="#pin" x="356" y="335"/>
    </g>
    <polygon class="window-glass" points="760,99 905,100 970,160 973,199 760,199"/>
    <text class="brand-name" x="54" y="167" textLength="680" lengthAdjust="spacingAndGlyphs" transform="rotate(10.4 54 167)">BOXWILLOW</text>
    <text class="service-line" x="50" y="209" textLength="630" lengthAdjust="spacingAndGlyphs" transform="rotate(12.1 50 209)">SEA PARCELS, AIR PARCELS, LOOSE CARGO IN CHINA TRADE LINE</text>
    <text class="phone-number" x="788" y="262" transform="rotate(8 788 262)">09 4815396</text>
    <text class="web-address" x="792" y="286" transform="rotate(8 792 286)">www.boxwillow.co.nz</text>
    <use class="outline" href="#van-shape"/>
  </g>
</svg>
</body>
</html>
```